Audio Tour Poster

I need a poster to show information on a audio tour ... walk ... bike etc ... the poster needs to be generic so that it could be used for several projects ... a space needs to be left to add a tour title and another area where a tri fold brochure can be placed for people to access ... the tri fold poster will be based on 8.5 x 14 inch legal size ...

The size of the final poster will be 18x 24 inches ... an example of a audio tour can be found at
http://trelvanu.com/walk/568 or http://trelvanu.com/walk/2507

Industry/Entity Type

Legal

```html
<!DOCTYPE html>
<html lang="en">
<head>
<meta charset="utf-8">
<title>Walking Audio Tour Poster</title>
<link rel="stylesheet" href="https://fonts.googleapis.com/css2?family=Marcellus&family=Questrial&display=swap">
<style>
  :root {
    --page: #ffffff;
    --sky: #d3e9e2;
    --earth: #47300d;
    --leaf-light: #bcd08f;
    --leaf-mid: #88a845;
    --holder-front: rgba(214, 214, 214, 0.6);
    --holder-edge: #3a3a3a;
    --white: #ffffff;
  }
  * { margin: 0; padding: 0; box-sizing: border-box; }
  html, body {
    width: 1200px; height: 1000px; overflow: hidden;
    background: var(--page);
  }
  .poster {
    position: absolute; left: 254px; top: 58px;
    width: 675px; height: 900px;
    background: var(--sky);
    overflow: hidden;
    color: var(--earth);
  }
  .headphones-icon {
    position: absolute; left: 284px; top: 48px;
    width: 104px; height: 104px;
  }
  .tour-title {
    position: absolute; left: 0; top: 168px; width: 100%;
    text-align: center;
    font-family: "Marcellus", serif;
    font-weight: 400;
    font-size: 86px;
    line-height: 84px;
    letter-spacing: 2px;
  }
  .tour-tagline {
    position: absolute; left: 0; top: 344px; width: 100%;
    text-align: center;
    font-family: "Questrial", sans-serif;
    font-size: 30px;
    letter-spacing: 0.5px;
  }
  .tour-features {
    position: absolute; left: 0; top: 405px; width: 100%;
    text-align: center;
    font-family: "Questrial", sans-serif;
    font-size: 17.5px;
    line-height: 23px;
  }
  .park-scene {
    position: absolute; left: 0; top: 482px;
    width: 100%; height: 283px;
    background: linear-gradient(to bottom, var(--leaf-light) 0%, var(--leaf-mid) 70%);
    clip-path: polygon(0 8%, 8% 0, 14% 12%, 20% 40%, 78% 40%, 84% 6%, 92% 2%, 100% 0, 100% 100%, 0 100%);
  }
  .ground-band {
    position: absolute; left: 0; top: 765px;
    width: 100%; height: 135px;
    background: var(--earth);
  }
  .brochure-slot {
    position: absolute; left: 257px; top: 495px;
    width: 156px; height: 312px;
    background: var(--white);
    border: 1px solid #555;
  }
  .brochure-holder {
    position: absolute; left: 249px; top: 572px;
    width: 174px; height: 249px;
    background: var(--holder-front);
    border: 1.5px solid var(--holder-edge);
  }
  .tour-footer {
    position: absolute; left: 0; top: 830px; width: 100%;
    display: flex; justify-content: center; align-items: center; gap: 22px;
    color: var(--white);
    font-family: "Questrial", sans-serif;
    font-size: 21px;
  }
  .speaker-icon { width: 56px; height: 46px; }
  .speaker-icon.is-mirrored { transform: scaleX(-1); }
</style>
</head>
<body>
  <main class="poster">
    <svg class="headphones-icon" viewBox="0 0 104 104" aria-hidden="true">
      <path d="M8 58 C8 8 96 8 96 58" fill="none" stroke="#47300d" stroke-width="5"/>
      <rect x="4" y="52" width="10" height="46" rx="3" fill="#47300d"/>
      <rect x="90" y="52" width="10" height="46" rx="3" fill="#47300d"/>
      <rect x="12" y="60" width="6" height="30" rx="2" fill="#47300d"/>
      <rect x="86" y="60" width="6" height="30" rx="2" fill="#47300d"/>
    </svg>

    <h1 class="tour-title">WALKING<br>AUDIO TOUR</h1>
    <p class="tour-tagline">(for however you get around)</p>
    <p class="tour-features">MP3 downloads direct to your smartphone<br>Geopositioning gives you infomation<br>at the right time</p>

    <div class="park-scene" role="img" aria-label="Green park trees with silhouettes of a family walking on the left and a cyclist riding on the right"></div>
    <div class="ground-band"></div>

    <div class="brochure-slot" aria-label="Brochure space"></div>
    <div class="brochure-holder"></div>

    <footer class="tour-footer">
      <svg class="speaker-icon" viewBox="0 0 56 46" aria-hidden="true">
        <path d="M2 15 H10 L22 5 V41 L10 31 H2 Z" fill="#fff"/>
        <path d="M29 14 Q34 23 29 32" fill="none" stroke="#fff" stroke-width="2.5"/>
        <path d="M36 8 Q44 23 36 38" fill="none" stroke="#fff" stroke-width="2.5"/>
        <path d="M43 2 Q54 23 43 44" fill="none" stroke="#fff" stroke-width="2.5"/>
      </svg>
      <span class="footer-note">This tour lorem ipsum dolor&nbsp; sit amet</span>
      <svg class="speaker-icon is-mirrored" viewBox="0 0 56 46" aria-hidden="true">
        <path d="M2 15 H10 L22 5 V41 L10 31 H2 Z" fill="#fff"/>
        <path d="M29 14 Q34 23 29 32" fill="none" stroke="#fff" stroke-width="2.5"/>
        <path d="M36 8 Q44 23 36 38" fill="none" stroke="#fff" stroke-width="2.5"/>
        <path d="M43 2 Q54 23 43 44" fill="none" stroke="#fff" stroke-width="2.5"/>
      </svg>
    </footer>
  </main>
</body>
</html>
```